Coffee Shop needs a fresh new menu

Hi,
I would like a new menu to be designed for our coffee shop.
We display our menu on a television screen, so would need it in a file that would allow us to continue to do so -- I have attached a photo so that you can see our current design, and how it is displayed.

I'd like something that is easy to read, if the design could have a "hipster" feel to it -- we are located at a hospital and University.

I have attached a Word file with what we would like on the menu.

Feel free to contact me if you have any questions.

Thanks,
Liv

Just A4 size will be fine, and no need to include menu 1 and menu 2 - I just put them in as an example of what we already have -- they are our printed menu's. Thanks

Hospital

```html
<!DOCTYPE html>
<html lang="en">
<head>
<meta charset="utf-8">
<title>Café Menu</title>
<link rel="stylesheet" href="https://fonts.googleapis.com/css2?family=Lato:wght@400&family=Stardos+Stencil:wght@700&display=swap">
<style>
  :root {
    --board-dark: #1c1c1c;
    --board-mid: #3a3a3a;
    --board-light: #4a4a4a;
    --chalk: #f2f2f2;
    --chalk-line: #e6e6e6;
  }
  * { margin: 0; padding: 0; box-sizing: border-box; }
  html, body { width: 848px; height: 1200px; overflow: hidden; }
  body {
    background: radial-gradient(ellipse at 50% 40%, var(--board-light) 0%, var(--board-mid) 45%, var(--board-dark) 100%);
    font-family: "Lato", sans-serif;
    color: var(--chalk);
  }
  .menu-board { position: relative; width: 848px; height: 1200px; }
  .chalk-frame { position: absolute; inset: 0; }
  .section-title {
    position: absolute;
    left: 0; width: 848px;
    text-align: center;
    font-family: "Stardos Stencil", serif;
    font-weight: 700;
    font-size: 30px;
    letter-spacing: 0.5px;
    text-transform: uppercase;
    line-height: 1;
    color: var(--chalk);
  }
  .menu-list {
    position: absolute;
    left: 218px; width: 420px;
    list-style: none;
    font-size: 21px;
    line-height: 32.3px;
  }
  .menu-item { display: flex; }
  .item-name { width: 357px; }
  .item-price { white-space: nowrap; }
</style>
</head>
<body>
<main class="menu-board">
  <svg class="chalk-frame" width="848" height="1200" viewBox="0 0 848 1200" fill="none" stroke="var(--chalk-line)" stroke-width="2.5" stroke-linecap="round">
    <!-- outer frame -->
    <path d="M272 45 H133 V1145 H718 V45 H578"/>
    <path d="M272 60 H150 V1160 H738 V60 H578" opacity="0.85"/>
    <!-- breakfast rule -->
    <path d="M45 369 H272 M578 369 H803"/>
    <path d="M45 383 H272 M578 383 H803" opacity="0.85"/>
    <!-- hot food rule -->
    <path d="M45 715 H200 M650 715 H803"/>
    <path d="M45 729 H200 M650 729 H803" opacity="0.85"/>
  </svg>

  <h2 class="section-title" style="top:37px">Something Light</h2>
  <ul class="menu-list" style="top:82px">
    <li class="menu-item"><span class="item-name">Mixed Yoghurts</span><span class="item-price">$5.50</span></li>
    <li class="menu-item"><span class="item-name">Chia Pudding</span><span class="item-price">$5.50</span></li>
    <li class="menu-item"><span class="item-name">Fruit Salad</span><span class="item-price">$5.50</span></li>
    <li class="menu-item"><span class="item-name">Bircher Muesli</span><span class="item-price">$5.50</span></li>
    <li class="menu-item"><span class="item-name">Protein Balls</span><span class="item-price">$4.00</span></li>
    <li class="menu-item"><span class="item-name">Banana Bread</span><span class="item-price">$4.50</span></li>
    <li class="menu-item"><span class="item-name">Muffins</span><span class="item-price">$4.50</span></li>
    <li class="menu-item"><span class="item-name">Slices</span><span class="item-price">$4.00</span></li>
  </ul>

  <h2 class="section-title" style="top:361px">Breakfast Items</h2>
  <ul class="menu-list" style="top:400px">
    <li class="menu-item"><span class="item-name">Bacon, Egg and Cheese Roll</span><span class="item-price">$6.00</span></li>
    <li class="menu-item"><span class="item-name">Ham and Cheese Toastie</span><span class="item-price">$5.00</span></li>
    <li class="menu-item"><span class="item-name">Cheese and Tomato Toastie</span><span class="item-price">$5.00</span></li>
    <li class="menu-item"><span class="item-name">Ham and Cheese Croissant</span><span class="item-price">$6.00</span></li>
    <li class="menu-item"><span class="item-name">Cheese and Tomato Croissant</span><span class="item-price">$5.50</span></li>
    <li class="menu-item"><span class="item-name">Plain Croissant</span><span class="item-price">$3.50</span></li>
    <li class="menu-item"><span class="item-name">Hash Brown</span><span class="item-price">$2.00</span></li>
    <li class="menu-item"><span class="item-name">2 Piece Toast</span><span class="item-price">$3.00</span></li>
    <li class="menu-item"><span class="item-name">2 Piece Rasin Toast</span><span class="item-price">$3.00</span></li>
  </ul>

  <h2 class="section-title" style="top:707px">Hot Food and Sandwiches</h2>
  <ul class="menu-list" style="top:746px">
    <li class="menu-item"><span class="item-name">Pre Made Sandwiches</span><span class="item-price">$6.50</span></li>
    <li class="menu-item"><span class="item-name">Pre Made Sandwiches</span><span class="item-price">$7.50</span></li>
    <li class="menu-item"><span class="item-name">Pre Made Focaccias</span><span class="item-price">$8.50</span></li>
    <li class="menu-item"><span class="item-name">Wraps</span><span class="item-price">$7.50</span></li>
    <li class="menu-item"><span class="item-name">Vegetarian Salad</span><span class="item-price">$7.50</span></li>
    <li class="menu-item"><span class="item-name">Meat/Seafood Salad</span><span class="item-price">$9.50</span></li>
    <li class="menu-item"><span class="item-name">Hot Chips</span><span class="item-price">$4.50</span></li>
    <li class="menu-item"><span class="item-name">Dim Sim</span><span class="item-price">$1.50</span></li>
    <li class="menu-item"><span class="item-name">Potato Cake</span><span class="item-price">$1.50</span></li>
    <li class="menu-item"><span class="item-name">Plain Hamburger</span><span class="item-price">$7.50</span></li>
    <li class="menu-item"><span class="item-name">Hamburger with the lot</span><span class="item-price">$9.00</span></li>
    <li class="menu-item"><span class="item-name">Chicken Schnitzel Burger</span><span class="item-price">$8.50</span></li>
  </ul>
</main>
</body>
</html>
```